Company Web Design Project

Vantor grids works in the market of renewable energy with energy monitoring systems.

Vantor-grid wants a light and easy company website that informs about our core business and our products as well as the company. The sites should work on multiple platforms. It should include pictures and possibilities for news.
You find elements and company information on the following links:

http://vantor-grid.example/english-version/index.htm
some productinformation you find on this site:
http://kelwatch.example/

Vantor-grid AG is also interested in a Powerpoint template that matches the new website design as well as businesscards and a letter template.

Some more information about the company.

Headquartered in Karlsruhe, Germany, Vantor-Grid AG manufactures hardware & software solutions for remote monitoring, analysis, and control of electrical installations, alarm systems, and other critical networks.

In addition, our company provides test, measurement, and control equipment for use in a wide range of industrial and biological processes.

Founded in the year 2000, Vantor-Grid AG has established a comprehensive service network. Our solutions and systems are in operation e.g. in Europe, USA, Brazil, and Asia.

Vantor-Grid's team of experienced engineers, physicists, and network specialists continuously develop innovative solutions for many key industries - particularly in the renewable energies field.

To ensure the operational safety of their plants by means of optimized real time fault analysis routines

for process optimization

for a measurable increase in yield from production and trade.

Our products are distributed globally via an international dealer network.

In the interest of our customers and their needs, our aim is to expand this dealer network even more.
Updates

Target Market(s)

large solar project companies like, large renewable energy investors, large wholesellers for renewable energy, producer of solar panels.

Industry/Entity Type

Electrical

Requirements
Must have
• responsive design for multiple platforms

```html
<!DOCTYPE html>
<html lang="en">
<head>
<meta charset="utf-8">
<title>Vantor Grid – Renewable Energy Monitoring</title>
<link rel="stylesheet" href="https://fonts.googleapis.com/css2?family=Source+Sans+3:wght@300;400;600&family=Open+Sans:wght@400;700&display=swap">
<style>
  :root{
    --paper:#f3f3f1;
    --ink:#222222;
    --muted:#8a8a8a;
    --body:#8f8f8f;
    --green:#17826a;
    --green-dark:#0f6e58;
    --panel:#4a4540;
    --panel-line:#5b5650;
    --nav:#6f6f6f;
    --faint:#c9c9c6;
  }
  *{box-sizing:border-box;margin:0;padding:0}
  html,body{width:1080px;height:1200px;overflow:hidden;background:var(--paper)}
  body{position:relative;font-family:"Source Sans 3",sans-serif;color:var(--ink)}
  .abs{position:absolute}

  /* header */
  .contact-bar{top:7px;right:78px;font-size:11.5px;color:var(--muted);display:flex;align-items:center;gap:6px}
  .contact-bar strong{color:var(--green);font-weight:600}
  .contact-bar .sep{width:1px;height:18px;background:#d4d4d2;margin:0 6px}
  .brand{left:72px;top:38px;display:flex;align-items:center;gap:10px}
  .brand-mark{width:34px;height:34px;background:var(--green)}
  .brand-name{font-size:30px;font-weight:600;color:#2b2b2b;letter-spacing:-.3px}
  .main-nav{top:56px;left:499px;display:flex;font-size:12.5px;color:var(--nav);text-transform:uppercase}
  .main-nav a{color:inherit;text-decoration:none;margin-right:31px}
  .main-nav a:last-child{margin-right:0}
  .main-nav a.active{color:var(--green);font-weight:600}

  /* hero */
  .hero{left:73px;top:119px;width:934px;height:336px;background:linear-gradient(180deg,#8eaec4 0%,#c8d7df 45%,#dfe0d6 62%,#56633f 78%,#3b4630 100%)}
  .hero-shadow{left:90px;top:452px;width:900px;height:14px;border-radius:50%;background:radial-gradient(ellipse at center,rgba(0,0,0,.28),rgba(0,0,0,0) 70%)}
  .hero-caption{left:458px;top:351px;width:533px;height:52px;background:rgba(70,70,70,.78);color:#fff;font-size:36px;padding:8px 0 0 37px;font-weight:400;line-height:1}
  .hero-caption b{font-weight:600}
  .hero-cta{left:806px;top:403px;width:185px;height:33px;background:var(--green);color:#fff;font-size:17px;padding:5px 0 0 32px}

  /* welcome */
  .section-mark{left:80px;top:505px;width:24px;height:30px;background:var(--green)}
  .welcome-title{left:124px;top:506px;font-size:24px;font-weight:400;color:#222}
  .welcome-title span{color:var(--green)}
  .lede{left:79px;top:558px;width:608px;font-family:"Open Sans",sans-serif;font-size:9.3px;line-height:12.7px;color:var(--body)}
  .lede p+p{margin-top:13px}

  .news-title{left:717px;top:509px;font-size:23px;font-weight:400;color:#222}
  .news{left:719px;width:285px;font-family:"Open Sans",sans-serif}
  .news time{display:block;font-family:"Source Sans 3",sans-serif;font-size:12.5px;color:var(--green);margin-bottom:5px}
  .news p{font-size:9.3px;line-height:12.7px;color:var(--body)}
  .news a{display:block;font-size:9.3px;font-weight:700;color:#222;text-decoration:none;margin-top:6px}

  .divider{left:73px;top:746px;width:934px;height:4px;background:radial-gradient(ellipse at center,rgba(0,0,0,.22),rgba(0,0,0,0) 70%)}

  /* products */
  .products{left:75px;top:789px;width:211px;height:283px;background:var(--panel);color:#fff}
  .products h2{font-size:19px;font-weight:400;padding:14px 0 0 21px;height:52px}
  .products ul{list-style:none}
  .products li{height:34px;border-top:1px solid var(--panel-line);font-size:11.5px;padding:8px 0 0 26px;position:relative;letter-spacing:.3px}
  .products li:first-child{border-top:none}
  .products li::before{content:"›";position:absolute;left:11px;top:6px;font-size:13px}

  /* feature columns */
  .feature{width:207px}
  .feature h3{font-size:19px;font-weight:400;color:var(--green);height:32px;margin-top:1px}
  .feature .photo{height:105px;margin-top:25px}
  .feature p{font-family:"Open Sans",sans-serif;font-size:9.3px;line-height:12.7px;color:var(--body);margin-top:20px;height:72px}
  .read-more{display:flex;width:114px;height:28px;text-decoration:none;margin-left:3px}
  .read-more span{flex:1;background:var(--panel);color:#fff;font-size:12.5px;padding:6px 0 0 13px}
  .read-more i{width:28px;background:var(--green);display:flex;align-items:center;justify-content:center}

  /* footer */
  .footer-line{left:73px;top:1128px;width:934px;height:1px;background:#e3e3e0}
  .footer-mark{left:77px;top:1144px;width:36px;height:40px;background:#c4c4c1}
  .footer-name{left:128px;top:1144px;font-size:15px;font-weight:300;color:#a8a8a6}
  .footer-copy{left:128px;top:1169px;font-size:10px;color:var(--faint)}
  .footer-nav{left:374px;top:1168px;display:flex;gap:28px;font-size:10px;color:var(--faint)}
  .footer-nav a{color:inherit;text-decoration:none}
  .social{left:917px;top:1153px;display:flex;gap:13px}
  .social span{width:20px;height:20px;background:#8a8a8a}
  .social span.round{border-radius:50%}
</style>
</head>
<body>

<header>
  <div class="abs contact-bar">
    <strong>hello@vantor-grid.example</strong> Email Us
    <span class="sep"></span>
    <strong>1800-555-014</strong> Call Us
  </div>
  <div class="abs brand">
    <span class="brand-mark"></span>
    <span class="brand-name">vantor-grid</span>
  </div>
  <nav class="abs main-nav">
    <a class="active" href="#">Home</a>
    <a href="#">About Us</a>
    <a href="#">Business Area</a>
    <a href="#">Products</a>
    <a href="#">Topical</a>
    <a href="#">Contact Us</a>
  </nav>
</header>

<section>
  <div class="abs hero" role="img" aria-label="Row of wind turbines on green hills under a bright cloudy sky"></div>
  <div class="abs hero-shadow"></div>
  <div class="abs hero-caption"><b>Lorem ipsum</b> is dummy text</div>
  <div class="abs hero-cta">Find out more &gt;&gt;</div>
</section>

<section>
  <div class="abs section-mark"></div>
  <h1 class="abs welcome-title">Welcome To <span>Vantor Grid</span></h1>
  <div class="abs lede">
    <p>Lorem ipsum dolor sit amet, consectetur adipiscing elit. Sed rhoncus faucibus faucibus. Maecenas erat odio, mattis id suscipit a, ullamcorper nec felis. Pellentesque ut sem et ante condimentum ultrices quis nec lorem. Integer non sem justo. Praesent malesuada, nulla id elementum aliquam, elit erat tincidunt justo, ut posuere erat metus eu turpis. Pellentesque habitant morbi tristique senectus et netus et malesuada fames ac turpis egestas. Donec tempus congue sem, sed volutpat justo mollis semper. Phasellus facilisis, dui sed elementum pretium, metus sapien scelerisque orci, ut accumsan nisi dui at felis. Integer pulvinar justo eu arcu rutrum ornare.</p>
    <p>Morbi semper adipiscing placerat. Donec viverra nisl faucibus arcu pellentesque et facilisis diam pulvinar. Vestibulum non arcu id ipsum viverra accumsan et eget magna. Nullam id nulla vel libero euismod pharetra non eu sem. Sed purus erat, sollicitudin sed tempus rhoncus, bibendum eget nunc. Morbi eu dignissim enim. Donec et arcu tellus, in pellentesque purus. In vitae rutrum ligula. Quisque vel ligula id urna placerat dictum. Pellentesque ut sem et ante condimentum ultrices quis nec lorem. Integer non sem justo. Praesent malesuada, nulla id elementum aliquam, elit erat tincidunt justo</p>
  </div>

  <h2 class="abs news-title">Latest News</h2>
  <article class="abs news" style="top:557px">
    <time>February 12th 2013</time>
    <p>Lorem ipsum dolor sep sit amet sed lorem ipsum onectur aispis cing eli consectetur adipiscing elit semper adipiscing placerat...</p>
    <a href="#">Read More...</a>
  </article>
  <article class="abs news" style="top:634px">
    <time>February 20th 2013</time>
    <p>Pellentesque ut sem et ante condimentum ultrices quis lorem. Integer non sem justo. Praesent malesuada, nulla id elementum aliquam, elit erat tincidunt justo</p>
    <a href="#">Read More...</a>
  </article>
</section>

<div class="abs divider"></div>

<section>
  <aside class="abs products">
    <h2>Our products</h2>
    <ul>
      <li>Pellentesque ut sem et ante</li>
      <li>Sem et ante condimentum</li>
      <li>Ultrices quis nec lorem.</li>
      <li>Integer sem justo praesent</li>
      <li>Pellentesque ut sem et ante</li>
      <li>Sem et ante condimentum</li>
      <li>Ultrices quis nec lorem.</li>
    </ul>
  </aside>

  <article class="abs feature" style="left:322px;top:800px">
    <h3>Our services</h3>
    <div class="photo" role="img" aria-label="Light bulb filled with green leaves on a soft grey background" style="background:linear-gradient(90deg,#b9bab4,#dadbd6 60%,#b7c59a)"></div>
    <p>Lorem ipsum dolor sit amet, consectetur piscing elit. Sed rhoncus faucibus faucibus. Maecenas et odio, mattis id suscipit a, ullamcorper nec felis. Pellentesque ut sem et ante condimentum.</p>
    <a class="read-more" href="#"><span>Read more</span><i><svg width="12" height="10" viewBox="0 0 12 10"><path d="M1 1l4 4-4 4M6 1l4 4-4 4" fill="none" stroke="#fff" stroke-width="1.2"/></svg></i></a>
  </article>

  <article class="abs feature" style="left:563px;top:800px">
    <h3>Our solutions</h3>
    <div class="photo" role="img" aria-label="Wind turbines standing on hills under a blue sky" style="background:linear-gradient(180deg,#7fa6c6,#cfdbe2 55%,#55633e 80%,#394529)"></div>
    <p>Lorem ipsum dolor sit amet, consectetur piscing elit. Sed rhoncus faucibus faucibus. Maecenas et odio, mattis id suscipit a, ullamcorper nec felis. Pellentesque ut sem et ante condimentum.</p>
    <a class="read-more" href="#"><span>Read more</span><i><svg width="12" height="10" viewBox="0 0 12 10"><path d="M1 1l4 4-4 4M6 1l4 4-4 4" fill="none" stroke="#fff" stroke-width="1.2"/></svg></i></a>
  </article>

  <article class="abs feature" style="left:800px;top:800px">
    <h3>Know the team</h3>
    <div class="photo" role="img" aria-label="Team members stacking their hands together in a circle" style="background:linear-gradient(135deg,#e6e3df,#c79e80 50%,#ece9e5)"></div>
    <p>Lorem ipsum dolor sit amet, consectetur piscing elit. Sed rhoncus faucibus faucibus. Maecenas et odio, mattis id suscipit a, ullamcorper nec felis. Pellentesque ut sem et ante condimentum.</p>
    <a class="read-more" href="#"><span>Read more</span><i><svg width="12" height="10" viewBox="0 0 12 10"><path d="M1 1l4 4-4 4M6 1l4 4-4 4" fill="none" stroke="#fff" stroke-width="1.2"/></svg></i></a>
  </article>
</section>

<footer>
  <div class="abs footer-line"></div>
  <div class="abs footer-mark"></div>
  <div class="abs footer-name">Vantor Grid</div>
  <div class="abs footer-copy">2013 All Rights Reserved</div>
  <nav class="abs footer-nav">
    <a href="#">Home</a><a href="#">About Us</a><a href="#">Contact Us</a><a href="#">Privacy Policy</a><a href="#">Sitemap</a>
  </nav>
  <div class="abs social" aria-label="Social links">
    <span></span><span class="round"></span><span></span>
  </div>
</footer>

</body>
</html>
```